Borealis Pictures are looking for a poster design for a new short film called "Paper Lantern"
The film will be submitted to all major film festivals so great exposure....

Paper Lantern was written and directed by Tom Ashworth. Produced by Borealis Pictures. Starring Rob Milner, Clara Whitby, Dan Ashworth, Neil Fairbank and Gareth Pym.

Synopsis: Paper Lantern, tells the story of Joe. A want-away agent/hit man for an undisclosed body, who is sent on a mysterious mission for his final assignment.
Whilst waiting on his last instructions in a hideaway, he meets Magda and Frank and begins to snatch at the real life he's craved for so long.
In danger of taking his eye off the ball too soon, Joe must kill time and fight loneliness, for just one more day.

To give you an feel for the film here is the trailer on Youtube http://www.clipvault-example.net/watch?v=qX7mTz2LpaR.

Please can you put borealis website www.borealispictures-example.co.uk on the design.

Best of luck

```html
<!DOCTYPE html>
<html lang="en">
<head>
<meta charset="utf-8">
<title>Paper Lantern — Poster</title>
<link href="https://fonts.googleapis.com/css2?family=Anton&family=Pathway+Gothic+One&display=swap" rel="stylesheet">
<style>
  :root {
    --ink-black: #050505;
    --wall-light: #5a5a5a;
    --wall-mid: #2a2a2a;
    --title-white: #ffffff;
    --blood-red: #a11d1b;
    --text-white: #f2f2f2;
  }
  * { margin: 0; padding: 0; box-sizing: border-box; }
  html, body {
    width: 842px; height: 1200px; overflow: hidden;
    background: var(--ink-black);
  }
  .poster {
    position: relative;
    width: 842px; height: 1200px;
    overflow: hidden;
    font-family: "Pathway Gothic One", "Oswald", sans-serif;
    color: var(--text-white);
  }
  .wall {
    position: absolute; inset: 0;
    background:
      radial-gradient(ellipse 470px 540px at 430px 660px,
        var(--wall-light) 0%, var(--wall-mid) 45%, var(--ink-black) 100%);
  }
  .cast {
    position: absolute; top: 68px; left: 0; right: 0;
    display: flex; justify-content: center; gap: 20px;
    font-size: 30px; line-height: 34px;
    list-style: none;
  }
  .cast .accent { color: var(--blood-red); }
  .credit {
    position: absolute; top: 290px; right: 82px;
    font-size: 36px; line-height: 40px;
  }
  .title {
    position: absolute; left: 0; top: 0;
    width: 842px; height: 1200px;
  }
  .title text {
    font-family: "Anton", "Impact", sans-serif;
  }
  .tagline {
    position: absolute; top: 838px; left: 370px;
    font-size: 30px; line-height: 34px;
  }
  .website {
    position: absolute; top: 1130px; right: 76px;
    font-family: "Anton", sans-serif;
    font-size: 20px; line-height: 26px; letter-spacing: 0.6px;
    color: var(--blood-red);
  }
</style>
</head>
<body>
<main class="poster">
  <div class="wall" role="img" aria-label="Dark wooden plank wall lit by a soft spotlight"></div>

  <ul class="cast">
    <li>Rob Milner</li>
    <li class="accent">Clara Whitby</li>
    <li>Dan Ashworth</li>
    <li class="accent">Neil Fairbank</li>
    <li>and Gareth Pym</li>
  </ul>

  <p class="credit">a Tom Ashworth film</p>

  <svg class="title" viewBox="0 0 842 1200" aria-label="Paper Lantern">
    <defs>
      <linearGradient id="greyFill" x1="0" y1="0" x2="0" y2="1">
        <stop offset="0" stop-color="#9c9c9c"/>
        <stop offset="0.75" stop-color="#c4c4c4"/>
        <stop offset="1" stop-color="#6a6a6a"/>
      </linearGradient>
      <linearGradient id="redFill" x1="0" y1="0" x2="1" y2="1">
        <stop offset="0" stop-color="#6e1210"/>
        <stop offset="1" stop-color="#a11d1b"/>
      </linearGradient>
    </defs>
    <text class="title-top" x="88" y="505" font-size="192"
          textLength="677" lengthAdjust="spacingAndGlyphs"
          fill="url(#greyFill)">PAPER</text>
    <text class="title-bottom" x="88" y="823" font-size="335"
          textLength="677" lengthAdjust="spacingAndGlyphs"><tspan fill="url(#redFill)">LAN</tspan><tspan fill="#ffffff">TERN</tspan></text>
  </svg>

  <p class="tagline">Fight loneliness, for just one more day...</p>

  <p class="website">www.borealispictures-example.co.uk</p>
</main>
</body>
</html>
```